Side of Page Partnership-type Letterhead Design for Chiropractic Office

Side oriented letterhead with practice locations/demographics, physician names and company logo

Target Market(s)

Healthcare Professionals & Attorneys

Industry/Entity Type

Healthcare

Font styles to use
Other font styles liked:
• Font of Logo is Trajan Pro, but not a deal breaker if we try something else

Colors

Designer to choose colors to be used in the design.

Requirements
Must have
• All info from attached documents

```html
<!DOCTYPE html>
<html lang="en">
<head>
<meta charset="utf-8">
<title>Keystone Chiropractic Letterhead</title>
<link href="https://fonts.googleapis.com/css2?family=Cinzel:wght@400&display=swap" rel="stylesheet">
<style>
  :root {
    --backdrop: #2b2b2d;
    --paper: #f1f1f1;
    --ink: #1c1c1c;
    --blue: #2b3d8f;
    --orange: #e08a2b;
    --green: #4e9a3a;
  }
  * { margin: 0; padding: 0; box-sizing: border-box; }
  html, body { width: 1200px; height: 780px; overflow: hidden; }
  body { background: var(--backdrop); font-family: "Cinzel", serif; color: var(--ink); }
  .letterhead {
    position: absolute; left: 338px; top: 20px;
    width: 523px; height: 740px;
    background: var(--paper);
  }
  .brand {
    position: absolute; left: 41px; top: 60px;
    display: flex; align-items: center; gap: 8px;
  }
  .brand-name {
    font-size: 13px; font-weight: 400; letter-spacing: 0.3px;
    color: var(--ink); white-space: nowrap;
  }
  .brand-mark { width: 28px; height: 28px; background: var(--blue); flex: none; }
  .physicians {
    position: absolute; right: 34px; top: 56px;
    list-style: none; text-align: right;
    font-size: 11.5px; line-height: 16.4px; letter-spacing: 0.3px;
  }
  .locations { position: absolute; top: 664px; left: 0; width: 100%; }
  .location {
    position: absolute; top: 0; font-style: normal;
    font-size: 8px; line-height: 11.4px; letter-spacing: 0; white-space: nowrap;
  }
  .location-city { display: block; }
  .location .label { margin-right: 2px; }
  .location-north { left: 167px; }
  .location-north .location-city, .location-north .label { color: var(--blue); }
  .location-maple { left: 284px; }
  .location-maple .location-city, .location-maple .label { color: var(--orange); }
  .location-cedar { left: 410px; }
  .location-cedar .location-city, .location-cedar .label { color: var(--green); }
  .color-bands { position: absolute; left: 162px; top: 730px; width: 337px; height: 10px; display: flex; }
  .band { flex: 1; }
  .band-blue { background: var(--blue); }
  .band-orange { background: var(--orange); }
  .band-green { background: var(--green); }
</style>
</head>
<body>
  <main class="letterhead">
    <header class="brand">
      <span class="brand-name">Keystone Chiropractic</span>
      <span class="brand-mark" aria-hidden="true"></span>
    </header>

    <ul class="physicians">
      <li>Daniel Voss, DC, DACNB</li>
      <li>Martin Voss, DC</li>
      <li>Kyle Denton, DC</li>
      <li>Evan Whitcomb, DC</li>
      <li>Noah Pellman, DC</li>
      <li>Lucas Brenner, DC</li>
      <li>Owen Tillery, DC</li>
    </ul>

    <footer class="locations">
      <address class="location location-north">
        <span class="location-city">Northgate</span>
        4120 N. Linden St.<br>
        Northgate, OH 43100<br>
        <span class="label">P:</span>555-210-4410<br>
        <span class="label">F:</span>555-210-4411
      </address>
      <address class="location location-maple">
        <span class="location-city">Maple Ridge</span>
        218 E. Grove St.<br>
        Maple Ridge, OH 43200<br>
        <span class="label">P:</span>555-318-2270<br>
        <span class="label">F:</span>555-318-2271
      </address>
      <address class="location location-cedar">
        <span class="location-city">Cedar Falls</span>
        752 W. Orchard Rd<br>
        Cedar Falls, OH 43300<br>
        <span class="label">P:</span>555-427-6630<br>
        <span class="label">F:</span>555-427-6631
      </address>
    </footer>

    <div class="color-bands">
      <span class="band band-blue"></span>
      <span class="band band-orange"></span>
      <span class="band band-green"></span>
    </div>
  </main>
</body>
</html>
```